TALVEXO needs a Sleek, Professional and Serious Web Design, this web design is aiming to be famous!

Dear Designers,

We need a web design for a new company based on the Internet named "talvexo". I have already worked with PQ to get my logo and it has been a wonderful experience which I want to repeat. We are kind of work social network, the web page will be mostly used to write comments on businesses around the world to help workers find which company fit the best for them. This website is also here to help people finding work by giving them the tools to make the right research.

For contents inspiration, you could see on the added files a sketch of the website but I am not asking you following it because it was just for giving the contents.

We do not have any example regarding website that we do like because all are coming so generic. We would like a very sleek website, where surfing become very intuitive and ergonomic (Glimmerly is not very ergonomic for example from our point of view). The website must reflect professionalism and seriousness and worker, world connexion.

We will be pleased to accept original designs as long as they fit to our requirements and if it is properly made of course: e.g. web page looking like a newspaper etc.

About colours, we are not decided yet but we are aiming a light orange (pastel style) or dark bluish green. Also, it comes to our attention that a web site mostly realized in grey-scale will be very interesting (touch of colour will be accepted as well if it miss too much dynamism) .

We will give the feedback as soon as possible because we would like to have 5 pages but it will be only very small changes on the next ones. (like adding 4 buttons)

Target Market(s)

Our target is relatively large because it is all people of working age, in numbers we can say a range of people aged from 18 to 45 years.

Industry/Entity Type

Internet

Number of Pages Required

3 page

Font styles to use
Sans Serif

Requirements
Must have
• Elements that must be on the web page are exposed below:
• - company logo ( .ai & .eps files on added files)
• - 4 buttons (Searcher "highlighted" / Advises / Jobs / Solutions)
• - login/account window
• - language button (e.g. a flag)
• - Window companies searcher (the most important, refer to the sketch)
• - classic menu down the page - about us / contact us / conditions / site map / community / politics / publicity / languages / copyright etc.
Nice to have
• We want a professional and serious website.
Should not have
• If you have a doubt, just ask us because nothing are coming to our mind.

```html
<!DOCTYPE html>
<html lang="en">
<head>
<meta charset="utf-8">
<title>TALVEXO — Companies Searcher</title>
<link rel="stylesheet" href="https://fonts.googleapis.com/css2?family=Oswald:wght@400;500&family=Open+Sans:ital,wght@0,400;0,600;1,400&family=Montserrat:wght@400;500&display=swap">
<style>
:root{
  --orange:#f7922e;
  --orange-dark:#e07a18;
  --ink:#2b2b2b;
  --ink-soft:#555;
  --muted:#8a8a8a;
  --panel:#f0f0f0;
  --section:#ededed;
  --white:#fff;
  --footer:#3b3b3b;
  --badge:#b9b9b9;
}
*{box-sizing:border-box;margin:0;padding:0}
html,body{width:1200px;height:1121px;overflow:hidden}
body{position:relative;background:var(--white);font-family:"Open Sans",Arial,sans-serif;color:var(--ink)}
.site-header{position:absolute;left:0;top:0;width:1200px;height:92px;background:var(--white)}
.brand{position:absolute;left:70px;top:30px;display:flex;align-items:center;gap:10px}
.brand-dot{width:26px;height:26px;border-radius:50%;background:var(--ink)}
.brand-name{font-family:"Oswald",sans-serif;font-weight:500;font-size:34px;letter-spacing:1px;color:var(--ink);line-height:1}
.top-bar{position:absolute;right:80px;top:15px;display:flex;align-items:center;gap:14px;font-size:12px}
.lang{display:flex;align-items:center;gap:4px;font-family:"Oswald",sans-serif;color:var(--muted)}
.lang-flag{width:12px;height:8px;background:linear-gradient(#b22 0 50%,#fff 50% 100%);border-left:5px solid #33a}
.phone{display:flex;align-items:center;gap:4px;font-family:"Montserrat",sans-serif;font-weight:500;font-size:14px;color:var(--ink)}
.main-nav{position:absolute;left:473px;top:47px;display:flex;gap:0}
.main-nav a{font-family:"Oswald",sans-serif;font-size:13px;color:#666;text-decoration:none;padding:5px 16px;line-height:17px;margin-right:0}
.main-nav a.active{background:#333;color:var(--white);margin-right:1px}
.account{position:absolute;left:1008px;top:45px;width:112px;height:31px;background:var(--orange);border-bottom:2px solid var(--orange-dark);color:var(--white);font-family:"Open Sans",sans-serif;font-weight:600;font-size:13px;display:flex;align-items:center;justify-content:center;gap:7px}
.hero{position:absolute;left:0;top:92px;width:1200px;height:445px;background:linear-gradient(180deg,#6e6c68 0%,#8d8a84 30%,#a9a39a 48%,#5d5751 70%,#3f3933 100%)}
.searcher{position:absolute;left:698px;top:145px;width:318px;height:317px;background:var(--panel);padding:14px 20px 0 20px}
.searcher h2{font-family:"Oswald",sans-serif;font-weight:500;font-size:25px;color:var(--ink);line-height:28px}
.searcher p{font-size:12.5px;color:#666;margin-top:3px}
.field{display:block;width:280px;height:29px;margin-top:19px;background:var(--white);border:1px solid #ddd;font-size:11.5px;color:#555;padding:6px 9px}
.field:first-of-type{margin-top:12px}
.enter{margin-top:21px;width:280px;height:31px;background:var(--orange);border-bottom:2px solid var(--orange-dark);color:var(--white);font-size:13px;display:flex;align-items:center;justify-content:center}
.what{position:absolute;left:0;top:537px;width:1200px;height:428px;background:var(--section)}
.what h1{position:absolute;left:0;top:42px;width:1200px;text-align:center;font-family:"Oswald",sans-serif;font-weight:400;font-size:29px;color:var(--ink)}
.what .lead{position:absolute;left:262px;top:84px;width:676px;text-align:center;font-style:italic;font-size:12px;line-height:19px;color:var(--muted)}
.service{position:absolute;top:160px;width:300px;text-align:center}
.service .disc{width:152px;height:152px;border-radius:50%;background:var(--white);margin:0 auto;box-shadow:1px 2px 2px rgba(0,0,0,.1);display:flex;align-items:center;justify-content:center}
.service .disc.highlight{background:var(--orange)}
.service h3{margin-top:26px;font-family:"Montserrat",sans-serif;font-weight:500;font-size:15px;color:#222}
.service p{margin-top:9px;font-size:11px;line-height:17px;color:#555}
.flow-arrow{position:absolute}
.partners{position:absolute;left:0;top:965px;width:1200px;height:112px;background:var(--white);display:flex;align-items:center;justify-content:center;gap:34px}
.partner{background:var(--badge);opacity:.7}
.site-footer{position:absolute;left:0;top:1077px;width:1200px;height:44px;background:var(--footer);color:var(--white);font-size:12.5px}
.copyright{position:absolute;left:182px;top:13px}
.footer-nav{position:absolute;right:180px;top:13px;display:flex;gap:11px}
.footer-nav a{color:var(--white);text-decoration:none}
</style>
</head>
<body>
<header class="site-header">
  <div class="brand"><span class="brand-dot"></span><span class="brand-name">TALVEXO</span></div>
  <div class="top-bar">
    <span class="lang"><span class="lang-flag"></span>EN ▾</span>
    <span class="phone"><svg width="11" height="11" viewBox="0 0 24 24"><path fill="#2b2b2b" d="M6.6 10.8a15 15 0 006.6 6.6l2.2-2.2c.3-.3.7-.4 1-.2 1.1.4 2.3.6 3.6.6.6 0 1 .4 1 1V20c0 .6-.4 1-1 1A17 17 0 013 4c0-.6.4-1 1-1h3.5c.6 0 1 .4 1 1 0 1.3.2 2.5.6 3.6.1.3 0 .7-.2 1z"/></svg>555-310-7724</span>
  </div>
  <nav class="main-nav">
    <a class="active" href="#">HOME</a><a href="#">COMPANY</a><a href="#">ADVISES</a><a href="#">JOBS</a><a href="#">SOLUTIONS</a><a href="#">ABOUT US</a><a href="#">CONTACT US</a>
  </nav>
  <div class="account"><span>Login</span><span>|</span><span>Sign Up</span></div>
</header>

<section class="hero" role="img" aria-label="Photo of business people walking along a waterfront boardwalk in front of a city skyline"></section>

<form class="searcher">
  <h2>COMPANIES SEARCHER</h2>
  <p>Lorem ipsum dolor sit amet consectetur...</p>
  <span class="field">Company Name VAT Number</span>
  <span class="field">City</span>
  <span class="field">Post Code</span>
  <span class="field">Country</span>
  <div class="enter">Enter</div>
</form>

<section class="what">
  <h1>What We Do?</h1>
  <p class="lead">Lorem ipsum dolor sit amet, consectetur adipiscing elit, sed do eiusmod tempor incididunt ut labore et dolore magna aliqua. Ut enim ad minim veniam, quis nostrud laboris nisi ut aliquip ex ea commodo consequat..</p>

  <svg class="flow-arrow" style="left:405px;top:185px" width="95" height="38" viewBox="0 0 95 38"><path d="M4 32 Q45 0 90 30" fill="none" stroke="#cfcfcf" stroke-width="2"/><path d="M82 22 L91 31 L80 34" fill="none" stroke="#cfcfcf" stroke-width="2"/></svg>
  <svg class="flow-arrow" style="left:705px;top:258px" width="100" height="40" viewBox="0 0 100 40"><path d="M4 30 Q55 40 96 6" fill="none" stroke="#cfcfcf" stroke-width="2"/><path d="M86 6 L97 5 L96 16" fill="none" stroke="#cfcfcf" stroke-width="2"/></svg>

  <div class="service" style="left:149px">
    <div class="disc"><svg width="80" height="80" viewBox="0 0 80 80"><circle cx="30" cy="36" r="14" fill="#333"/><path d="M6 76 Q8 54 30 54 Q52 54 54 76Z" fill="#333"/><circle cx="56" cy="20" r="14" fill="none" stroke="#333" stroke-width="3"/><rect x="54.5" y="17" width="3" height="11" fill="#333"/><circle cx="56" cy="12.5" r="2" fill="#333"/></svg></div>
    <h3>TALVEXO ADVISES</h3>
    <p>Lorem Ipsum is simply dummy text of the printing<br>and typesetting industry.</p>
  </div>
  <div class="service" style="left:453px">
    <div class="disc highlight"><svg width="60" height="76" viewBox="0 0 60 76"><rect x="14" y="2" width="32" height="34" rx="4" fill="#fff"/><rect x="3" y="22" width="6" height="20" rx="2" fill="#fff"/><rect x="51" y="22" width="6" height="20" rx="2" fill="#fff"/><rect x="10" y="40" width="40" height="10" rx="3" fill="#fff"/><rect x="28" y="50" width="4" height="12" fill="#fff"/><rect x="10" y="62" width="40" height="4" fill="#fff"/><circle cx="12" cy="71" r="2.5" fill="#fff"/><circle cx="24" cy="71" r="2.5" fill="#fff"/><circle cx="36" cy="71" r="2.5" fill="#fff"/><circle cx="48" cy="71" r="2.5" fill="#fff"/></svg></div>
    <h3>TALVEXO JOBS</h3>
    <p>Lorem Ipsum is simply dummy text of the printing<br>and typesetting industry.</p>
  </div>
  <div class="service" style="left:752px">
    <div class="disc"><svg width="90" height="80" viewBox="0 0 90 80"><circle cx="36" cy="34" r="16" fill="#333"/><path d="M6 78 Q8 54 36 54 Q64 54 66 78Z" fill="#333"/><circle cx="62" cy="22" r="15" fill="none" stroke="#333" stroke-width="8" stroke-dasharray="5 3.5"/><circle cx="62" cy="22" r="11" fill="none" stroke="#333" stroke-width="5"/></svg></div>
    <h3>TALVEXO SOLUTIONS</h3>
    <p>Lorem Ipsum is simply dummy text of the printing<br>and typesetting industry.</p>
  </div>
</section>

<section class="partners" aria-label="Partners">
  <div class="partner" style="width:68px;height:50px"></div>
  <div class="partner" style="width:136px;height:34px"></div>
  <div class="partner" style="width:58px;height:54px"></div>
  <div class="partner" style="width:82px;height:60px"></div>
  <div class="partner" style="width:58px;height:58px;border-radius:50%"></div>
  <div class="partner" style="width:118px;height:40px"></div>
  <div class="partner" style="width:96px;height:30px"></div>
</section>

<footer class="site-footer">
  <span class="copyright">© Copyright talvexo.comAll Right Reserved</span>
  <nav class="footer-nav">
    <a href="#">About us</a><a href="#">Contact us</a><a href="#">Community</a><a href="#">Publicity</a><a href="#">Conditions</a><a href="#">Politics</a><a href="#">Language</a>
  </nav>
</footer>
</body>
</html>
```